CD Cover Design Project

Although I posted a picture as a possible idea, an idea from scratch is mostly what I am looking for. Definitely listen to the song before making the design. The link is posted right here in the project overview.
I need a CD cover for my latest single. This artwork will go up on Melodeck, brimora, etc with the song. Please listen to the song and then creat the artwork. Here is a link to the song:
http://tunevaultmusic.net/doriancolewhitfield/where-the-rivers-bend
The design needs my name, Dorian Cole Whitfield and it needs the song title, Where the Rivers Bend.
It needs to be a perfect square.
1600 by 1600
Resolution 300 DPI
Contact me at dorian@dorian-cole.net or (503) 482-3091

```html
<!DOCTYPE html>
<html lang="en">
<head>
<meta charset="utf-8">
<title>Where the Rivers Bend – Dorian Cole Whitfield</title>
<link rel="stylesheet" href="https://fonts.googleapis.com/css2?family=Great+Vibes&family=Pinyon+Script&display=swap">
<style>
  :root {
    --night: #05050a;
    --night-soft: #1a1820;
    --haze: #2c2830;
    --moon-light: #b9bccb;
    --moon-mid: #6e7185;
    --beam-blue: rgba(70, 80, 200, 0.28);
    --beam-violet: rgba(110, 40, 150, 0.35);
    --chrome-hi: #ffffff;
    --chrome-mid: #c9c9d2;
    --chrome-low: #7b7b86;
    --chrome-edge: #2a2a33;
    --grass: #5a4f7a;
  }
  html, body {
    margin: 0;
    padding: 0;
    width: 1200px;
    height: 1200px;
    overflow: hidden;
    background: var(--night);
  }
  .cover {
    position: relative;
    width: 1200px;
    height: 1200px;
    overflow: hidden;
    background: var(--night);
  }
  .backdrop-photo {
    position: absolute;
    inset: 0;
    background:
      radial-gradient(ellipse 40% 30% at 20% 30%, var(--haze), transparent 70%),
      radial-gradient(ellipse 35% 30% at 80% 25%, var(--haze), transparent 70%),
      radial-gradient(ellipse 40% 35% at 85% 65%, var(--night-soft), transparent 70%),
      radial-gradient(ellipse 45% 35% at 30% 70%, var(--night-soft), transparent 70%),
      var(--night);
  }
  .moon-photo {
    position: absolute;
    left: 440px;
    top: 240px;
    width: 420px;
    height: 650px;
    border-radius: 50%;
    background: radial-gradient(ellipse 45% 50% at 35% 50%, var(--moon-light), var(--moon-mid) 45%, transparent 75%);
  }
  .light-beams {
    position: absolute;
    inset: 0;
  }
  .grass-strip {
    position: absolute;
    left: 0;
    bottom: 0;
    width: 1200px;
    height: 56px;
    background: linear-gradient(to bottom, transparent, var(--grass));
  }
  .chrome-type {
    position: absolute;
    left: 0;
    width: 1200px;
    margin: 0;
    text-align: center;
    white-space: nowrap;
    font-weight: 400;
    background: linear-gradient(to bottom, var(--chrome-hi) 10%, var(--chrome-mid) 45%, var(--chrome-low) 55%, var(--chrome-hi) 85%);
    -webkit-background-clip: text;
    background-clip: text;
    color: transparent;
    -webkit-text-stroke: 1.5px var(--chrome-edge);
    filter: drop-shadow(0 2px 3px rgba(0,0,0,0.8));
  }
  .song-title {
    top: 70px;
    font-family: "Great Vibes", cursive;
    font-size: 128px;
    line-height: 1.2;
  }
  .artist-name {
    top: 1010px;
    font-family: "Pinyon Script", cursive;
    font-size: 118px;
    line-height: 1.2;
    -webkit-text-stroke: 3px var(--chrome-edge);
  }
</style>
</head>
<body>
  <main class="cover">
    <div class="backdrop-photo" role="img" aria-label="Dark, faded overlapping portrait photographs forming the night background"></div>
    <div class="moon-photo" role="img" aria-label="Photograph of a crescent moon"></div>
    <svg class="light-beams" width="1200" height="1200" viewBox="0 0 1200 1200" aria-hidden="true">
      <polygon points="835,210 290,700 530,1070" fill="var(--beam-blue)"/>
      <polygon points="205,810 10,965 1200,1060" fill="var(--beam-violet)"/>
    </svg>
    <div class="grass-strip" role="img" aria-label="Silhouette of grass along the bottom edge"></div>
    <h1 class="chrome-type song-title">Where the Rivers Bend</h1>
    <p class="chrome-type artist-name">Dorian Cole Whitfield</p>
  </main>
</body>
</html>
```